Stayvora Waterfront Home Postcard

Hello

I have recently placed my house on Stayvora and would like to use the very nice pictures I already have available to get postcards for my guests so they have a souvenir and it also becomes a advertisement tool. Can you help me?

Thank you
Marisol

Target Market(s)

Holiday makers looking for a wildlife sanctuary

Industry/Entity Type

House

Font styles to use
Script

Colors

Designer to choose colors to be used in the design.

Requirements
Must have
• Water front Home on one of the Crest Isles near Brisbane beautifully furnished and appointed for $30/night (on the basis of x4 people sharing) sleeps max. 6 people

Book through Stayvora: www.stayvora.example/rooms/4392071 and your friendly host will give you more details
Nice to have
• If it is possible to also have some of the other pictures

```html
<!DOCTYPE html>
<html lang="en">
<head>
<meta charset="utf-8">
<title>Stayvora Waterfront Home Postcard</title>
<link rel="stylesheet" href="https://fonts.googleapis.com/css2?family=Montserrat:wght@700&family=Nunito+Sans:ital,wght@0,400;0,600;0,700;0,800;1,400;1,700&display=swap">
<style>
  :root {
    --stage: #000000;
    --card: #ffffff;
    --accent-red: #e0202a;
    --ink: #5a4a45;
    --ink-soft: #6b5f5b;
    --bar: #5a3a32;
    --bar-text: #ffffff;
    --band-start: #f4ece6;
    --band-end: #e6d8ce;
    --quote-mark: #d8c8bd;
  }
  * { box-sizing: border-box; margin: 0; padding: 0; }
  html, body { width: 782px; height: 1200px; overflow: hidden; background: var(--stage); }
  .canvas { position: relative; width: 782px; height: 1200px; background: var(--stage); font-family: "Nunito Sans", Arial, sans-serif; }

  .card { position: absolute; left: 36px; width: 709px; background: var(--card); }
  .card--front { top: 45px; height: 547px; }
  .card--back { top: 607px; height: 548px; }

  .photo { position: absolute; }
  .photo--living { left: 18px; top: 16px; width: 493px; height: 355px; background: linear-gradient(160deg, #b79ac8 0%, #e7d79a 35%, #d86a3e 60%, #c9a58a 100%); }
  .photo--bay { left: 520px; top: 16px; width: 172px; height: 112px; background: linear-gradient(180deg, #5a8fc2 0%, #3f79ae 55%, #3f6b2e 75%, #1e241c 100%); }
  .photo--bedroom { left: 520px; top: 136px; width: 172px; height: 114px; background: linear-gradient(160deg, #8d6bb0 0%, #b49ac8 45%, #f1ece8 100%); }
  .photo--kitchen { left: 520px; top: 257px; width: 172px; height: 114px; background: linear-gradient(160deg, #d9683f 0%, #f2d6bf 60%, #c79a63 100%); }

  .photo--turtle { left: 18px; top: 19px; width: 172px; height: 114px; background: linear-gradient(180deg, #1b3d3c 0%, #2f5653 60%, #1a302f 100%); }
  .photo--birds { left: 196px; top: 19px; width: 172px; height: 114px; background: linear-gradient(180deg, #4e6a3a 0%, #8a9a6e 50%, #e6e2dc 100%); }
  .photo--sunset { left: 18px; top: 141px; width: 172px; height: 114px; background: linear-gradient(180deg, #7a1e0c 0%, #e2532a 40%, #f08a3a 55%, #2a1208 100%); }
  .photo--beach { left: 196px; top: 141px; width: 172px; height: 114px; background: linear-gradient(180deg, #1f55b6 0%, #6fa0e0 45%, #d9d3c2 70%, #cfc3a6 100%); }

  .info-band { position: absolute; left: 18px; top: 377px; width: 674px; height: 150px; background: linear-gradient(90deg, var(--band-start) 0%, var(--band-end) 100%); }
  .listing-title { position: absolute; left: 12px; top: 9px; width: 340px; font-family: "Montserrat", Arial, sans-serif; font-weight: 700; font-size: 16.5px; line-height: 17px; color: var(--accent-red); text-transform: uppercase; }
  .listing-body { position: absolute; left: 12px; top: 45px; width: 405px; font-size: 13.4px; line-height: 17px; color: var(--ink-soft); }

  .price { position: absolute; left: 432px; top: 30px; width: 232px; text-align: center; color: var(--ink); }
  .price__lead { font-weight: 700; font-size: 15px; line-height: 18px; }
  .price__amount { font-weight: 800; font-size: 37px; line-height: 40px; letter-spacing: -0.3px; }
  .price__note { font-size: 12.2px; line-height: 15px; color: var(--ink-soft); }

  .book-bar {
    position: absolute; left: 18px; height: 29px;
    padding: 0 24px 0 10px;
    background: var(--bar); color: var(--bar-text);
    font-size: 13px; line-height: 29px; white-space: nowrap;
    clip-path: polygon(0 0, calc(100% - 12px) 0, 100% 50%, calc(100% - 12px) 100%, 0 100%);
  }
  .book-bar b { font-weight: 800; }
  .card--front .book-bar { top: 499px; }
  .card--back .book-bar { top: 502px; }

  .review__mark { position: absolute; }
  .review__mark--open { left: 36px; top: 298px; }
  .review__mark--close { left: 325px; top: 439px; }
  .review__text { position: absolute; left: 74px; top: 297px; width: 266px; font-style: italic; font-size: 9.5px; line-height: 14px; color: var(--ink-soft); }
  .review__author { font-weight: 700; display: block; }
</style>
</head>
<body>
<div class="canvas">

  <section class="card card--front">
    <div class="photo photo--living" role="img" aria-label="Open-plan living room with wicker sofas, red throw and kitchen behind"></div>
    <div class="photo photo--bay" role="img" aria-label="View through the windows across the lawn to the bay with a sailing boat"></div>
    <div class="photo photo--bedroom" role="img" aria-label="Bedroom with purple walls and a white double bed"></div>
    <div class="photo photo--kitchen" role="img" aria-label="Kitchen with orange wall and timber benchtop"></div>

    <div class="info-band">
      <h1 class="listing-title">Waterfront home on one of the Crest Isles near Brisbane</h1>
      <p class="listing-body">Our beautifully designed 3 bedroom, 2 bathroom home also has a very large (50m2) veranda overlooking a level lawn that takes you to a little sandy beach. At high tide you can swim or launch the canoe. You can also hand feed the birds as we do !</p>
      <div class="price">
        <p class="price__lead">Appointed for</p>
        <p class="price__amount">$30/night</p>
        <p class="price__note">(on the basis of x4 people sharing)<br>sleeps max. 6 people</p>
      </div>
    </div>

    <div class="book-bar"><b>Book through Stayvora:</b> www.stayvora.example/rooms/4392071</div>
  </section>

  <section class="card card--back">
    <div class="photo photo--turtle" role="img" aria-label="Turtle swimming in dark water beside a hand"></div>
    <div class="photo photo--birds" role="img" aria-label="Cockatoo and lorikeets feeding on the terrace"></div>
    <div class="photo photo--sunset" role="img" aria-label="Orange sunset over the bay with palm silhouettes"></div>
    <div class="photo photo--beach" role="img" aria-label="Sandy beach under a blue sky"></div>

    <svg class="review__mark review__mark--open" width="28" height="24" viewBox="0 0 28 24" aria-hidden="true">
      <path d="M0 24V13C0 6 3 1.5 10 0l1.5 3C8 4.5 6.5 7 6.5 10H12v14zM16 24V13c0-7 3-11.5 10-13l1.5 3C24 4.5 22.5 7 22.5 10H28v14z" fill="var(--quote-mark)"/>
    </svg>
    <p class="review__text">Our group of 4 stayed for 4 days in this beautiful house. The place is amazing: birds on the terrace all day long that you can feed, sunset front of the terrace, sea at the end of the backyard. A huge living room with an open kitchen fully equiped. Not only is the place priceless, but Marisol is the nicest host you could have. A very friendly wildlife enthusiast, who knows perfectly how to receive. She can recommend a lot of excursions to do, and places to go in the area, like boat trips on stradbroke island, peel island, where you may see dolphins, turtles and so much more! We definitely recommend the place!<span class="review__author">- Corinne</span></p>
    <svg class="review__mark review__mark--close" width="28" height="24" viewBox="0 0 28 24" aria-hidden="true">
      <path d="M28 0v11c0 7-3 11.5-10 13l-1.5-3C20 19.5 21.5 17 21.5 14H16V0zM12 0v11c0 7-3 11.5-10 13L.5 21C4 19.5 5.5 17 5.5 14H0V0z" fill="var(--quote-mark)"/>
    </svg>

    <div class="book-bar"><b>Book through Stayvora:</b> www.stayvora.example/rooms/4392071</div>
  </section>

</div>
</body>
</html>
```